Old Fashioned, Artisan Goat Milk Soap Label

We are branching out in our goat milk dairy into artisan goat milk soaps. High quality, yet an old fashioned feel. Simple yet elegant. Emphasis on the milk and its moisturizing, healing, softening, and superiority.
Purity in a simple design that harkens back to a quaint, earlier time where quality ingredients were valued as much as quality workmanship.
Perhaps a drop symbolizing the milk, or a bucket pouring into or out of the logo. We already have our farm logo, Willowbrook Hollow, and were thinking the soap would be "Sweet Nell"
The labels will grace our liquid soap bottles and our bar soaps. 3.5" X 2.5"
The label color will be an antiqued ivory or other shade to convey a simpler time.

Reason: Realized that the contest length was short enough to scare away designers. Adding time to give entered designers time to create.

Target Market(s)

Upscale people looking to know where their products come from. People looking for better options, artisan products.

Requirements
Must have
• My project must have emphasis on the milk, old time feel, simple elegance
Nice to have
• Perhaps a drop symbolizing the milk, or a bucket pouring into or out of the logo. We already have our farm logo, Willowbrook Hollow, and were thinking the soap would be "Sweet Nell"
• If you use a goat, please be aware that we have the breed Nubians that have long luxurious ears and don't have horns.

```html
<!DOCTYPE html>
<html lang="en">
<head>
<meta charset="utf-8">
<title>Sweet Nell Goats Milk Soap Label</title>
<link rel="stylesheet" href="https://fonts.googleapis.com/css2?family=Almendra+Display&family=Pirata+One&family=Questrial&display=swap">
<style>
  :root {
    --backdrop: #ffffff;
    --ivory: #f3edcb;
    --ivory-deep: #e9e1b8;
    --ink: #1c2046;
  }
  html, body {
    margin: 0;
    padding: 0;
    width: 1200px;
    height: 898px;
    overflow: hidden;
    background: var(--backdrop);
  }
  .canvas {
    position: relative;
    width: 1200px;
    height: 898px;
  }
  .label {
    position: absolute;
    left: 50px;
    top: 19px;
    width: 1100px;
    height: 860px;
    background: linear-gradient(180deg, var(--ivory) 0%, var(--ivory-deep) 100%);
  }
  .frame {
    position: absolute;
    left: 21px;
    top: 101px;
    width: 1057px;
    height: 745px;
    border: 3px solid var(--ink);
    box-sizing: border-box;
  }
  .frame::after {
    content: "";
    position: absolute;
    inset: 8px;
    border: 1.5px solid var(--ink);
  }
  .farm-mark {
    position: absolute;
    left: 77px;
    top: 205px;
    width: 400px;
    text-align: center;
    color: var(--ink);
    font-family: "Questrial", sans-serif;
  }
  .farm-name {
    font-size: 40px;
    letter-spacing: 1px;
    line-height: 1;
  }
  .farm-place {
    margin-top: 10px;
    font-size: 13px;
    letter-spacing: 2px;
  }
  .product-name {
    position: absolute;
    margin: 0;
    color: var(--ink);
    font-family: "Almendra Display", serif;
    font-weight: 400;
    line-height: 1;
    white-space: nowrap;
  }
  .product-name--first {
    left: 86px;
    top: 420px;
    font-size: 190px;
    transform: rotate(-8deg);
    transform-origin: left center;
  }
  .product-name--second {
    left: 620px;
    top: 250px;
    font-size: 160px;
    transform: rotate(-5deg);
    transform-origin: left center;
  }
  .milk-drop {
    position: absolute;
    left: 550px;
    top: 450px;
  }
  .product-type {
    position: absolute;
    left: 300px;
    top: 608px;
    width: 690px;
    text-align: center;
    margin: 0;
    color: var(--ink);
    font-family: "Pirata One", serif;
    font-weight: 400;
    font-size: 78px;
    line-height: 1;
  }
  .double-rule {
    position: absolute;
    left: 84px;
    top: 703px;
    width: 959px;
    height: 9px;
    border-top: 3px solid var(--ink);
    border-bottom: 3px solid var(--ink);
  }
  .purity-note {
    position: absolute;
    left: 84px;
    top: 745px;
    width: 900px;
    margin: 0;
    color: var(--ink);
    font-family: "Questrial", sans-serif;
    font-size: 35px;
    line-height: 1;
    white-space: nowrap;
  }
</style>
</head>
<body>
<div class="canvas">
  <div class="label">
    <div class="frame"></div>

    <div class="farm-mark">
      <div class="farm-name">WILLOWBROOK HOLLOW</div>
      <div class="farm-place">MILLBROOK, TX</div>
    </div>

    <h1 class="product-name product-name--first">Sweet</h1>
    <h1 class="product-name product-name--second">Nell</h1>

    <svg class="milk-drop" width="400" height="100" viewBox="0 0 400 100" aria-hidden="true">
      <path d="M10 62 Q90 50 180 60" fill="none" stroke="#1c2046" stroke-width="3"/>
      <path d="M220 60 Q300 50 390 62" fill="none" stroke="#1c2046" stroke-width="3"/>
      <path d="M200 10 C188 34 176 48 176 66 A24 24 0 0 0 224 66 C224 48 212 34 200 10 Z" fill="#1c2046"/>
      <path d="M189 64 A12 12 0 0 0 198 80" fill="none" stroke="#f3edcb" stroke-width="3"/>
    </svg>

    <p class="product-type">Goats milk soap</p>

    <div class="double-rule"></div>

    <p class="purity-note">No extra additives, colors, or fragrances</p>
  </div>
</div>
</body>
</html>
```